Proposal Document Template for New Accounting and Tax Clients

Hi Farid,
We hope you are well.
We are an Accounting Firm based in the suburb of Pyrmont near Sydney city, and you recently designed a Package Title page for us that we use when providing our clients their year end statements and tax returns.

Because we like the design so much, we would like to work with you again. We would like you to incorporate aspects of your original Package Title Page design throughout our Proposal Document to provide design consistency between both documents.

We need our Proposal Document to be a fully editable Word document, as we send it to potential new clients to win their business and we will need to adjust what we include to suit each one.

We also think it could work if the design includes key images from our website.

We have two key brand colours:
Blue - Hex code #021738
Gold - Hex code #b2a98c

I have included:
- New Tormella Advisory Title Page_050225 - this was your previous design that we would like the Proposal Document to look similar to
- Proposal Document_V2_Detailed_Leo - this is our current Proposal Document that we would like you to redesign, keeping the content, but updating the design to look consistent with the New Tormella Advisory Title Page.
- Our Logo in different colours in JPEG Format (I also have PNG and EPS files of these. If you need them, please let me know)
- The key images from our website www.tormella.net.au

Please let me know if you have any questions or need anything further.

Thank you in advance
Jo
Updates

We received the designs one day ago, that combined with the Easter Holiday break means we need more time to review and provide feedback.

Target Market(s)

Accounting, Tax, and Strategic Business Planning Clients from Small Business, to Corporates , and Individuals

Industry/Entity Type

Accounting

Font styles to use
Other font styles liked:
• Calibri

Requirements
Must have
• Our logo and the ability to edit the document
Nice to have
• Include images from our website tormella.net.au

```html
<!DOCTYPE html>
<html lang="en">
<head>
<meta charset="UTF-8">
<title>Services Proposal – Tormella Advisory</title>
<link href="https://fonts.googleapis.com/css2?family=Poppins:wght@400;500;800&display=swap" rel="stylesheet">
<style>
  :root {
    --navy: #021738;
    --navy-band: #0b1f45;
    --gold: #b2a98c;
    --white: #ffffff;
    --paper: #f7f7f8;
    --sky-top: #c9cfe3;
    --sky-mid: #dde1ea;
    --city: #5d7590;
    --ground: #a9a394;
  }
  * { margin: 0; padding: 0; box-sizing: border-box; }
  html, body { width: 848px; height: 1200px; overflow: hidden; background: var(--white); }
  .cover {
    position: relative;
    width: 848px;
    height: 1200px;
    overflow: hidden;
    font-family: 'Poppins', sans-serif;
  }
  .cover-photo {
    position: absolute;
    inset: 0;
    background: linear-gradient(180deg, var(--sky-top) 0%, var(--sky-mid) 38%, var(--city) 62%, var(--ground) 85%, #8f8a7e 100%);
  }
  .cover-shapes { position: absolute; inset: 0; }
  .title {
    position: absolute;
    left: 66px;
    top: 84px;
    color: var(--navy);
    line-height: 1;
  }
  .title-light {
    display: block;
    font-weight: 500;
    font-size: 87px;
    letter-spacing: 1px;
  }
  .title-bold {
    display: block;
    font-weight: 800;
    font-size: 90px;
    margin-top: 0;
    letter-spacing: 0;
  }
  .date-tag {
    position: absolute;
    left: 67px;
    top: 953px;
    width: 141px;
    height: 28px;
    border: 1px solid var(--gold);
    color: var(--gold);
    font-size: 13px;
    font-weight: 500;
    letter-spacing: 0.5px;
    display: flex;
    align-items: center;
    justify-content: center;
  }
  .contact {
    position: absolute;
    left: 67px;
    color: var(--white);
    font-size: 15px;
    font-weight: 400;
    line-height: 19px;
  }
  .contact-address { top: 995px; }
  .contact-lines { top: 1052px; font-size: 15.5px; }
  .contact-lines .divider { margin: 0 10px; }
  .brand {
    position: absolute;
    left: 548px;
    top: 1010px;
    color: var(--navy);
    font-weight: 500;
    font-size: 27px;
    line-height: 32px;
    white-space: nowrap;
  }
</style>
</head>
<body>
  <main class="cover">
    <div class="cover-photo" role="img" aria-label="Photograph of the Sydney city skyline with glass towers and cranes seen from a harbourside park with stone steps and trees"></div>

    <svg class="cover-shapes" width="848" height="1200" viewBox="0 0 848 1200" aria-hidden="true">
      <polygon points="848,798 426,998 848,1200" fill="var(--paper)"/>
      <polygon points="0,800 848,1194 848,1200 0,1200" fill="var(--white)"/>
      <polygon points="0,806 848,1200 0,1200" fill="var(--navy-band)"/>
    </svg>

    <h1 class="title">
      <span class="title-light">SERVICES</span>
      <span class="title-bold">PROPOSAL</span>
    </h1>

    <div class="date-tag">7 JANUARY 2025</div>

    <p class="contact contact-address">Address: Level 4, Suite 12,<br>18 Harbourline Road, Pyrmont NSW 2009</p>
    <p class="contact contact-lines">Call: +612 9000 4100<span class="divider">|</span>Visit: tormella.net.au</p>

    <div class="brand">Tormella Advisory</div>
  </main>
</body>
</html>
```